A4 fitness centre email specials brochure

Quorel Signal Works have been providing audio visual services and support to fitness centres and health clubs for more than 10 years. We are seen as the "to-go" company for anything to do with Audio visual equipment yet we do not produce marketing material or promotional material for these customers so this is our first attempt at promotion. We wish to produce a PDF brochure suitable for emailing to existing and new clients promoting our products and services with special offers using the text contact on the attached draft. The brochure is simple but should carry the company logo in a prominant position, our corporate blue colour, and be easily read. a good photo can be used as a shaded backgound.

Target Market(s)

Health Club managers, fitness instructors

Industry/Entity Type

Fitness Equipment

Font styles to use
Sans Serif

Colors
0455a3

Requirements
Must have
• our corporate colour (blue) a good tag headline (Eg- AV fitness specials) and be easy to read. The brochure will be used as a PDF flyer to attach to emails and may also be printed to mail in some cased
Nice to have
• a picture of a gym with AV equipment in the background, maybe as a water mark image or faded. The brochure should reflect the fitness industry in order to grasp attention to our audience If space allows, maybe just have our offices mentioned in the contact details such as.... Melbourne-Brisbane-Sydney-Perth
Should not have
• don't want it to look cheap - we are the market leader for this sector for over 10 years and it should look professional

```html
<!DOCTYPE html>
<html lang="en">
<head>
<meta charset="utf-8">
<title>Complete Fitness Studio Audio Systems – Quorel Signal Works</title>
<link rel="stylesheet" href="https://fonts.googleapis.com/css2?family=Roboto:wght@300;400;500&family=Open+Sans:wght@400&display=swap">
<style>
  :root {
    --corporate-blue: #0455a3;
    --teal: #1f8aa0;
    --teal-deep: #155f70;
    --hero-dark: #2b3337;
    --ink: #222;
    --footer-bg: #1b1b1b;
    --footer-text: #2a6cc4;
    --white: #fff;
  }
  html, body { margin: 0; padding: 0; overflow: hidden; }
  body { width: 848px; height: 1200px; background: var(--white); font-family: "Roboto", sans-serif; color: var(--ink); }
  .flyer { position: relative; width: 848px; height: 1200px; overflow: hidden; }

  .hero { position: absolute; left: 0; top: 0; width: 848px; height: 558px; overflow: hidden; }
  .hero-backdrop { position: absolute; inset: 0; background: linear-gradient(160deg, #4a5357 0%, var(--hero-dark) 55%, #1d2326 100%); }
  .hero-shapes { position: absolute; inset: 0; }
  .product-lineup { position: absolute; left: 148px; top: 44px; width: 564px; height: 280px;
    background: radial-gradient(ellipse at center, rgba(60,66,72,0.85) 0%, rgba(40,44,48,0.6) 60%, rgba(40,44,48,0) 100%); border-radius: 8px; }
  .headline { position: absolute; left: 0; right: 0; top: 385px; margin: 0; text-align: center;
    font-weight: 300; font-size: 42px; line-height: 68px; color: var(--white); letter-spacing: 0.5px; }

  .intro { position: absolute; left: 0; right: 0; top: 640px; margin: 0; text-align: center;
    font-weight: 300; font-size: 16px; line-height: 43px; }
  .package-list { position: absolute; left: 0; right: 0; top: 764px; margin: 0; padding: 0; list-style: none;
    text-align: center; font-weight: 300; font-size: 16px; line-height: 43px; }

  .price-banner { position: absolute; left: 182px; top: 1022px; width: 495px; height: 61px; background: var(--corporate-blue);
    color: var(--white); display: flex; align-items: center; justify-content: center; gap: 14px; font-weight: 300; font-size: 29px; }
  .price-banner .price { font-weight: 500; font-size: 40px; }

  .footer { position: absolute; left: 0; bottom: 0; width: 848px; height: 32px; background: var(--footer-bg);
    font-family: "Open Sans", sans-serif; font-size: 12px; color: var(--footer-text); display: flex; align-items: center; }
  .brand { display: flex; align-items: center; gap: 7px; margin-left: 22px; }
  .brand-square { width: 12px; height: 12px; background: var(--teal); }
  .footer-contacts { margin-left: auto; margin-right: 18px; white-space: pre; }
</style>
</head>
<body>
<main class="flyer">
  <section class="hero">
    <div class="hero-backdrop" role="img" aria-label="Faded photo of a gym studio with audio equipment"></div>
    <svg class="hero-shapes" width="848" height="558" viewBox="0 0 848 558">
      <polygon points="0,200 284,30 560,300 560,558 0,558" fill="var(--teal)" opacity="0.55"/>
      <polygon points="0,472 284,30 0,30" fill="var(--hero-dark)" opacity="0.0"/>
      <polygon points="560,300 848,30 848,330 560,558" fill="var(--teal)" opacity="0.5"/>
      <polygon points="0,200 284,30 430,175 150,470 0,472" fill="var(--teal-deep)" opacity="0.35"/>
    </svg>
    <div class="product-lineup" role="img" aria-label="Product lineup: two speakers, wireless receiver and headset microphone, power amplifier, audio mixer and CD/media player"></div>
    <h1 class="headline">COMPLETE FITNESS STUDIO<br>AUDIO SYSTEMS</h1>
  </section>

  <p class="intro">Need to update your tired and unreliable audio system – Quorel Signal Works have a complete<br>range of systems or can customise a package to suit your exact requirements.</p>

  <ul class="package-list">
    <li>2 x 250 watt amplifier ( 2 yr warranty)</li>
    <li>2x Corvane 10” 250 watt speakers</li>
    <li>Fitness Series Audio mixer</li>
    <li>Professional fitness wireless microphone system</li>
    <li>Fitness instructors wireless headmi</li>
  </ul>

  <div class="price-banner"><span>All for just</span><span class="price">$2740</span><span>plus GST</span></div>

  <footer class="footer">
    <div class="brand"><span class="brand-square"></span><span>Quorel Signal Works</span></div>
    <div class="footer-contacts">Melbourne   Sydney   Brisbane   Perth  |  1300 418 562  |  www.quorelsignal.com.au  |  hello@quorelsignal.com.au</div>
  </footer>
</main>
</body>
</html>
```